Top New England Restaurant Needs Website Redesign

We currently have a website, rmsbistro.com, but would like to redesign it. We are a casual upscale restaurant specializing in breakfast and lunch. We are one of the top rated restaurants in all of New England and would like our site to look like it as well. We'd love to have a blog/news section that will be updated weekly or so, as well as an email capture feature on the page.

The site will mostly be static, with lots of pictures (I'll take them and provide). The only part of the site that will get updated regularly is the blog and/or news (could be the same page).

Some restaurant websites I like are: www.corvinmeade.com, www.brickandsage.com,

Target Market(s)

Foodies, RM's Bistro customers,

Industry/Entity Type

Restaurant

Logo Text

RM's Bistro

Font styles to use
Sans Serif

Requirements
Must have
• Chatterly Like Box, Rateo Box, Email capture, Blog/News, About Us page, Contact page

```html
<!DOCTYPE html>
<html lang="en">
<head>
<meta charset="utf-8">
<title>RM's Bistro</title>
<link rel="stylesheet" href="https://fonts.googleapis.com/css2?family=Sansita:wght@700;800&family=Open+Sans:wght@400;600;700&family=Playfair+Display:wght@900&display=swap">
<style>
:root{
  --orange:#f5921e;
  --orange-deep:#e9761a;
  --dark:#2d2622;
  --darker:#221d1a;
  --footer:#3a3836;
  --teal:#2aa9c8;
  --white:#ffffff;
  --ink:#333333;
  --muted:#777777;
  --cream:#fdf3e6;
}
*{margin:0;padding:0;box-sizing:border-box}
html,body{width:1200px;height:3480px;overflow:hidden}
body{position:relative;font-family:"Open Sans",sans-serif;color:var(--ink);background:var(--white)}
.abs{position:absolute}
.heading{font-family:"Sansita",sans-serif;font-weight:800}

/* hero */
.hero{left:0;top:0;width:1200px;height:800px;background:radial-gradient(circle at 75% 35%,#8a5a34 0%,#4a2f1e 40%,#241812 80%)}
.hero-plate{left:560px;top:0;width:640px;height:620px;border-radius:0 0 0 320px;background:radial-gradient(circle at 60% 45%,#f6d36a 0%,#e9e2d4 18%,#a46a3d 45%,rgba(60,35,20,0) 75%)}
.brand{left:40px;top:22px;display:flex;align-items:center;gap:12px;font-family:"Sansita",sans-serif;font-weight:800;font-size:40px;color:var(--white)}
.brand-dot{width:18px;height:18px;border-radius:50%;background:var(--teal)}
.menu-btn{left:1124px;top:20px;width:52px;height:52px;border-radius:50%;background:var(--teal);display:flex;flex-direction:column;justify-content:center;align-items:center;gap:6px}
.menu-btn span{width:24px;height:3px;background:var(--white);border-radius:2px}
.hero-title{left:92px;top:360px;font-family:"Playfair Display",serif;font-weight:900;font-size:56px;line-height:60px;color:var(--white);letter-spacing:1px}

/* about */
.about-band{left:0;top:640px;width:1200px;height:800px}
.about-box{left:160px;top:740px;width:400px;height:360px;border:2px solid rgba(255,255,255,.85);padding:30px 34px;color:var(--white)}
.about-box h2{font-size:44px;text-align:center;margin-bottom:22px}
.about-box p{font-size:14px;line-height:22px;margin-bottom:14px}
.btn-small{display:inline-block;border:1px solid var(--white);font-size:12px;font-weight:700;padding:4px 12px;letter-spacing:.5px}
.chef-photo{left:580px;top:780px;width:440px;height:360px;background:linear-gradient(160deg,#f2efe9 0%,#c7a98c 45%,#6d5646 100%);clip-path:polygon(3% 6%,20% 0,55% 4%,92% 1%,100% 20%,97% 60%,100% 94%,70% 100%,30% 97%,0 100%,2% 55%)}
.chef-caption{left:600px;top:1050px;color:var(--white)}
.chef-caption small{display:block;font-size:14px;font-weight:600}
.chef-caption strong{font-family:"Sansita",sans-serif;font-weight:800;font-size:28px}

/* feature */
.feature{left:0;top:1360px;width:1200px;height:560px;background:linear-gradient(180deg,var(--dark),var(--darker))}
.card{width:460px;height:340px;border:2px solid rgba(255,255,255,.8);padding:18px 16px}
.card h3{font-size:46px;color:var(--white);text-align:center;margin-bottom:14px}
.card-photo{height:190px}
.card-bar{height:40px;background:var(--teal);color:var(--white);font-size:13px;font-weight:700;display:flex;align-items:center;justify-content:space-between;padding:0 14px;letter-spacing:.5px}
.coffee{left:140px;top:1420px}
.coffee .card-photo{background:linear-gradient(135deg,#d6c5ac,#6b4a33 60%,#3a2a20)}
.menu-card{left:620px;top:1420px}
.menu-card .card-photo{background:linear-gradient(135deg,#f4e0b8,#c98a3e 55%,#7a4a22)}

/* blog */
.blog-band{left:0;top:1860px;width:1200px;height:620px}
.blog-title{left:0;top:1985px;width:1200px;text-align:center;font-size:52px;color:var(--white)}
.post{width:300px;height:330px;background:var(--white)}
.post-photo{height:150px;background:linear-gradient(180deg,#e9e6e1,#b9aa98 60%,#7d6b5b)}
.post-date{left:14px;top:120px;width:52px;height:60px;background:var(--orange);color:var(--white);text-align:center;font-size:11px;font-weight:700;line-height:14px;padding-top:6px}
.post-date b{display:block;font-size:22px;line-height:24px}
.post-body{padding:34px 16px 0}
.post-body h4{font-size:15px;font-weight:700;margin-bottom:10px}
.post-body p{font-size:12px;line-height:18px;color:var(--muted)}
.post-1{left:80px;top:2080px}
.post-2{left:450px;top:2080px}
.post-3{left:820px;top:2080px}

/* social */
.social-band{left:0;top:2440px;width:1200px;height:620px}
.social-title{font-size:30px;color:var(--ink)}
.social-box{width:510px;height:320px;border:1px solid #cfcfcf;background:var(--white)}
.chatterly-box{left:72px;top:2600px;padding:14px}
.chatterly-cover{height:120px;background:linear-gradient(135deg,#c7b8a5,#7d6450)}
.chatterly-name{font-weight:700;font-size:15px;margin:10px 0 8px}
.chatterly-grid{display:grid;grid-template-columns:repeat(10,1fr);gap:4px}
.chatterly-grid span{height:40px;background:linear-gradient(180deg,#b8a899,#6f5e50)}
.rateo-box{left:612px;top:2600px}
.rateo-head{height:44px;background:#c4201a;color:var(--white);font-weight:700;font-size:20px;display:flex;align-items:center;padding-left:16px;gap:10px}
.rateo-head i{width:12px;height:12px;background:var(--white);display:block}
.review{display:flex;gap:12px;padding:12px 16px;border-bottom:1px solid #eee}
.review-photo{width:48px;height:48px;background:linear-gradient(135deg,#c9b39c,#6d5444)}
.review b{font-size:13px}
.stars{display:flex;gap:3px;margin:4px 0}
.stars span{width:12px;height:12px;background:var(--orange)}
.review p{font-size:11px;color:var(--muted)}

/* footer */
.footer{left:0;top:3000px;width:1200px;height:480px}
.mail-badge{left:570px;top:3014px;width:60px;height:60px;border-radius:50%;background:var(--orange);display:flex;align-items:center;justify-content:center}
.f-col{top:3180px;color:#ddd}
.f-col h5{font-size:14px;font-weight:700;color:var(--white);letter-spacing:.5px;margin-bottom:22px}
.f-item{display:flex;gap:14px;margin-bottom:18px;font-size:13px;line-height:19px}
.f-item b{display:block;color:var(--white);font-size:12px}
.contact{left:72px;width:300px}
.newsletter{left:430px;width:340px;text-align:center}
.newsletter p{font-size:13px;line-height:19px;margin-bottom:14px}
.sub-form{display:flex;height:36px}
.sub-form span{flex:1;background:var(--white);color:#999;font-size:12px;text-align:left;padding:9px 10px}
.sub-form b{background:var(--orange);color:var(--white);font-size:12px;padding:10px 12px}
.social-icons{display:flex;gap:10px;justify-content:center;margin-top:22px}
.social-icons span{width:30px;height:30px;border:1px solid #bbb;border-radius:50%}
.hours{left:880px;width:260px}
.hours p{font-size:13px;margin-bottom:14px}
.hours b{display:block;color:var(--white);font-size:12px}
.map{width:200px;height:70px;background:linear-gradient(135deg,#e8e3da,#cfc7ba)}
.copyright{left:0;top:3440px;width:1200px;text-align:center;font-size:12px;color:#aaa}
.divider{top:3170px;width:1px;height:240px;background:#555}
</style>
</head>
<body>

<section class="hero abs" role="img" aria-label="Breakfast table with fried egg, toast and tomatoes"></section>
<div class="hero-plate abs"></div>
<div class="brand abs"><span class="brand-dot"></span>RM's Bistro</div>
<div class="menu-btn abs"><span></span><span></span><span></span></div>
<h1 class="hero-title abs">LOREM IPSUM<br>DOLOR SIT AMET</h1>

<svg class="about-band abs" viewBox="0 0 1200 800" preserveAspectRatio="none">
  <path d="M0 120 C300 30 800 30 1200 70 L1200 720 L0 720 Z" fill="var(--orange)"/>
</svg>
<div class="about-box abs">
  <h2 class="heading">About Us</h2>
  <p>RM's Bistro is committed to superior food quality and cultivating a pleasurable and welcoming dining experience, aiming to bring a fresh, local approach to breakfast and lunch in New England.</p>
  <p>From the warm welcome our guests receive as they walk through our doors, to the last bite of one of our savory dishes, we plan to take the dining experience you'd find in a classic bistro to the next level.</p>
  <span class="btn-small">READ MORE</span>
</div>
<div class="chef-photo abs" role="img" aria-label="Owner chef in white uniform and toque"></div>
<div class="chef-caption abs"><small>Owner</small><strong>Chef Marco Dellan</strong></div>

<section class="feature abs" role="img" aria-label="Dim café interior background"></section>
<div class="card coffee abs">
  <h3 class="heading">Our Coffee</h3>
  <div class="card-photo" role="img" aria-label="Barista serving coffee at the counter"></div>
  <div class="card-bar">READ MORE <span>&#8594;</span></div>
</div>
<div class="card menu-card abs">
  <h3 class="heading">Our Menu</h3>
  <div class="card-photo" role="img" aria-label="Stack of pancakes with syrup"></div>
  <div class="card-bar">EXPLORE OUR MENU <span>&#8594;</span></div>
</div>

<svg class="blog-band abs" viewBox="0 0 1200 620" preserveAspectRatio="none">
  <path d="M0 40 C400 0 800 0 1200 60 L1200 620 L0 620 Z" fill="var(--orange-deep)"/>
</svg>
<h2 class="blog-title heading abs">Recent Blog</h2>
<article class="post post-1 abs">
  <div class="post-photo" role="img" aria-label="Chef plating a dish"></div>
  <div class="post-date abs"><b>22</b>JUN 2015</div>
  <div class="post-body"><h4>Enter As Strangers, Leave As Friends</h4><p>Working in the hospitality business for as long as my father and I have, I sometimes think I can no longer be amazed however...</p></div>
</article>
<article class="post post-2 abs">
  <div class="post-photo" role="img" aria-label="Chef plating a dish"></div>
  <div class="post-date abs"><b>22</b>JUN 2015</div>
  <div class="post-body"><h4>Enter As Strangers, Leave As Friends</h4><p>Working in the hospitality business for as long as my father and I have, I sometimes think I can no longer be amazed however...</p></div>
</article>
<article class="post post-3 abs">
  <div class="post-photo" role="img" aria-label="Chef plating a dish"></div>
  <div class="post-date abs"><b>22</b>JUN 2015</div>
  <div class="post-body"><h4>Enter As Strangers, Leave As Friends</h4><p>Working in the hospitality business for as long as my father and I have, I sometimes think I can no longer be amazed however...</p></div>
</article>

<svg class="social-band abs" viewBox="0 0 1200 620" preserveAspectRatio="none">
  <path d="M0 80 C400 0 800 0 1200 80 L1200 620 L0 620 Z" fill="var(--white)"/>
</svg>
<h3 class="social-title heading abs" style="left:72px;top:2540px">Like Us On Chatterly</h3>
<h3 class="social-title heading abs" style="left:612px;top:2540px">Like Us On Rateo</h3>
<div class="social-box chatterly-box abs">
  <div class="chatterly-cover" role="img" aria-label="Bistro page cover photo"></div>
  <div class="chatterly-name">RM's Bistro</div>
  <div class="chatterly-grid" role="img" aria-label="Follower profile thumbnails">
    <span></span><span></span><span></span><span></span><span></span><span></span><span></span><span></span><span></span><span></span>
    <span></span><span></span><span></span><span></span><span></span><span></span><span></span><span></span><span></span><span></span>
  </div>
</div>
<div class="social-box rateo-box abs">
  <div class="rateo-head"><i></i>Rateo</div>
  <div class="review"><div class="review-photo" role="img" aria-label="Dish photo"></div><div><b>RM's Bistro</b><div class="stars"><span></span><span></span><span></span><span></span><span></span></div><p>Veggie scramble and home fries were highly recommended</p></div></div>
  <div class="review"><div class="review-photo" role="img" aria-label="Dish photo"></div><div><b>RM's Bistro</b><div class="stars"><span></span><span></span><span></span><span></span><span></span></div><p>Veggie scramble and home fries were highly recommended</p></div></div>
  <div class="review"><div class="review-photo" role="img" aria-label="Dish photo"></div><div><b>RM's Bistro</b><div class="stars"><span></span><span></span><span></span><span></span><span></span></div><p>Veggie scramble and home fries were highly recommended</p></div></div>
</div>

<svg class="footer abs" viewBox="0 0 1200 480" preserveAspectRatio="none">
  <path d="M0 60 C400 10 800 10 1200 60 L1200 480 L0 480 Z" fill="var(--footer)"/>
</svg>
<div class="mail-badge abs">
  <svg width="30" height="22" viewBox="0 0 30 22"><rect x="1" y="1" width="28" height="20" rx="2" fill="none" stroke="#fff" stroke-width="2"/><path d="M1 2 L15 13 L29 2" fill="none" stroke="#fff" stroke-width="2"/></svg>
</div>

<div class="f-col contact abs">
  <h5>CONTACT INFORMATION</h5>
  <div class="f-item"><svg width="16" height="20" viewBox="0 0 16 20"><path d="M8 0a7 7 0 0 0-7 7c0 5 7 13 7 13s7-8 7-13a7 7 0 0 0-7-7z" fill="#bbb"/><circle cx="8" cy="7" r="2.5" fill="#3a3836"/></svg><div><b>ADDRESS</b>RM's Bistro, 214 Harbor St<br>Salem, MA 01970</div></div>
  <div class="f-item"><svg width="16" height="18" viewBox="0 0 16 18"><path d="M3 1l3 4-2 2c1 3 3 5 6 6l2-2 4 3-2 3C7 17 0 10 1 3z" fill="#bbb"/></svg><div><b>PHONE</b>508-555-0142</div></div>
  <div class="f-item"><svg width="16" height="12" viewBox="0 0 16 12"><rect x="0.5" y="0.5" width="15" height="11" fill="none" stroke="#bbb"/><path d="M0.5 1L8 7l7.5-6" fill="none" stroke="#bbb"/></svg><div><b>EMAIL</b>info@rmsbistro.com</div></div>
</div>
<div class="divider abs" style="left:400px"></div>
<div class="f-col newsletter abs">
  <h5>SUBSCRIBE TO OUR NEWSLETTER</h5>
  <p>Subscribe to our mailing list and stay up to date with news, coupons, events + more!</p>
  <div class="sub-form"><span>Enter your e-mail address</span><b>SUBSCRIBE</b></div>
  <div class="social-icons"><span></span><span></span><span></span><span></span></div>
</div>
<div class="divider abs" style="left:830px"></div>
<div class="f-col hours abs">
  <h5>HOURS</h5>
  <p><b>TUESDAY TO SUNDAY</b>07:00 AM - 03:00 PM</p>
  <p><b>MONDAY</b>Closed</p>
  <div class="map" role="img" aria-label="Small location map"></div>
</div>
<p class="copyright abs">Copyright &copy; 2016 RM's Bistro. All Rights Reserved</p>

</body>
</html>
```